Dawson's Lawn Service needs a postcard design

I need a design to attract lawn cutting customers. I am a high school junior, focusing on my city and the neighboring city. I think it would be advantageous to let my potential clients know I am earning money for my college education. They should also know, I will be working side by side with my father, who operated his own lawn service for 20 years, so they can be assured of a quality result for their lawn. I will be using state of the art, commercial equipment.

A few things that are unique to my service are; my mower weighs half of what other commercial mowers do (a softer footprint), my mower does NOT throw clippings into mulch or flower beds, at an additional charge I offer bagging of the clippings and/or dog waste clean-up. I am thinking about a two-sided design. I would also like a cartoon style picture of myself riding my mower. If this is something you can create, I can send you a photo of myself and a photo of my mower. If not, I can get this drawing done separately, then send it to you, I would just need to know what kind of file you would need it in. I am not going to have a business name, I want to introduce myself as Dawson to keep it simple and personal. We can add a coupon to the postcard, offering one free cut with commitment to a full 26 week season. The name of my high school is Marwick High.

The cartoon picture attached is our logo.

Target Market(s)

Homeowners that use a commercial lawn cutting service, homeowners that need a temporary service while they are on vacation

Industry/Entity Type

School

Colors
3176b5
9bcb3c

Requirements
Must have
• An appeal for people to want to help me earn money for my college education. A clear idea they will be getting top notch service. I definitely want a drawing of myself on my mower. Phone # 555-271-0936
• design must work with parcelrelay.com/routeblanketmail guidelines

```html
<!DOCTYPE html>
<html lang="en">
<head>
<meta charset="utf-8">
<title>Dawson's Lawn Cutting Service – Postcard</title>
<link rel="stylesheet" href="https://fonts.googleapis.com/css2?family=Jost:wght@400;500&family=Yanone+Kaffeesatz:wght@400;500&family=Arimo:wght@700&display=swap">
<style>
  :root {
    --stage: #2d2d2d;
    --white: #ffffff;
    --grass: #7cb83a;
    --grass-light: #9bcb3c;
    --forest: #2f6b2f;
    --band: #3f9a3c;
    --brand-blue: #2b3a9c;
    --ink: #1f2a1a;
    --sky: #3f8fd6;
    --line: #555555;
  }
  * { margin: 0; padding: 0; box-sizing: border-box; }
  html, body { width: 960px; height: 1200px; overflow: hidden; }
  body { background: var(--stage); position: relative; font-family: "Jost", sans-serif; }

  .card { position: absolute; left: 128px; width: 705px; height: 545px; overflow: hidden; }
  .card--front { top: 33px; }
  .card--back { top: 626px; background: var(--white); }

  /* Front */
  .scene-art {
    position: absolute; inset: 0;
    background: linear-gradient(180deg, #4c9be0 0%, #8cc3ee 28%, #2f6fb0 34%, #5f8f3a 42%, #6ea83a 60%, #4f8a2a 100%);
  }
  .rider-art {
    position: absolute; left: 45px; top: 75px; width: 300px; height: 470px;
    background: radial-gradient(ellipse at 50% 55%, #b8a060 0%, #6a6a6a 45%, rgba(200,70,80,0.55) 70%, rgba(0,0,0,0) 78%);
  }
  .college-band {
    position: absolute; left: 412px; top: 237px; width: 293px; height: 86px;
    background: linear-gradient(90deg, rgba(63,154,60,0.75), var(--band));
    font-family: "Yanone Kaffeesatz", sans-serif; font-weight: 400;
    color: var(--ink); font-size: 29px; line-height: 35px; text-transform: uppercase;
    padding: 8px 0 0 28px;
  }
  .front-title {
    position: absolute; left: 364px; top: 330px;
    font-family: "Arimo", sans-serif; font-weight: 700; color: var(--white);
    font-size: 45px; line-height: 56px; text-shadow: 2px 2px 3px rgba(0,0,0,0.55);
  }
  .free-cut {
    position: absolute; left: 365px; top: 503px;
    font-family: "Arimo", sans-serif; font-weight: 700; color: var(--white);
    font-size: 20px; text-shadow: 1px 1px 2px rgba(0,0,0,0.5);
  }

  /* Back */
  .panel-shape { position: absolute; left: 0; top: 0; }
  .service-tag {
    position: absolute; left: 0; top: 25px; width: 269px; height: 47px;
    background: var(--forest); border-bottom: 3px solid var(--grass-light);
    font-family: "Yanone Kaffeesatz", sans-serif; font-weight: 500;
    color: var(--white); font-size: 33px; line-height: 45px; padding-left: 44px;
  }
  .logo-badge {
    position: absolute; left: 305px; top: 25px; width: 104px; height: 104px; border-radius: 50%;
    background: radial-gradient(circle at 50% 55%, #9a9a70 0%, #1f6aa5 55%, #175a92 100%);
  }
  .feature-list, .extras-list { position: absolute; left: 20px; list-style: none; }
  .feature-list { top: 98px; }
  .extras-list { top: 272px; }
  .feature-list li, .extras-list li {
    position: relative; padding-left: 24px; color: var(--ink);
    font-size: 16px; line-height: 22px; margin-bottom: 8px;
  }
  .extras-list li { margin-bottom: 5px; }
  .feature-list b, .extras-list b { font-weight: 500; color: var(--white); }
  .tick { position: absolute; left: 0; top: 4px; width: 14px; height: 14px; }
  .extras-heading {
    position: absolute; left: 44px; top: 236px;
    font-family: "Arimo", sans-serif; font-weight: 700; color: var(--brand-blue); font-size: 23px;
  }
  .season-offer {
    position: absolute; left: 38px; top: 364px; color: var(--white);
    font-size: 20px; line-height: 28px; letter-spacing: 0.3px;
  }
  .phone {
    position: absolute; left: 36px; top: 428px; display: flex; align-items: center; gap: 10px;
    color: var(--brand-blue); font-size: 30px; font-weight: 500; letter-spacing: 0.5px;
  }
  .stamp-box { position: absolute; left: 578px; top: 33px; width: 92px; height: 106px; border: 1px solid var(--line); }
  .address-line { position: absolute; left: 449px; width: 221px; height: 1px; background: var(--line); }
</style>
</head>
<body>

<section class="card card--front">
  <div class="scene-art" role="img" aria-label="Photo of a manicured lawn with palm trees and flower beds beside the sea under a blue sky"></div>
  <div class="rider-art" role="img" aria-label="Cartoon illustration of Dawson in a Marwick High baseball shirt riding a red zero-turn mower"></div>
  <div class="college-band">Help me earn money for<br>my college education</div>
  <h1 class="front-title">Dawson's<br>Lawn Cutting<br>Service</h1>
  <p class="free-cut">ASK ME ABOUT A FREE CUT</p>
</section>

<section class="card card--back">
  <svg class="panel-shape" width="705" height="545" viewBox="0 0 705 545">
    <path d="M0,0 H316 C380,45 412,160 410,285 C408,385 388,445 362,481 H0 Z" fill="var(--grass-light)"/>
    <path d="M0,0 H306 C370,45 402,160 400,285 C398,385 378,445 352,481 H0 Z" fill="var(--forest)"/>
    <path d="M0,0 H294 C356,45 388,160 386,285 C384,385 364,445 338,481 H0 Z" fill="var(--grass)"/>
    <rect x="0" y="481" width="184" height="64" fill="var(--grass)"/>
  </svg>

  <div class="service-tag">Dawson's Service</div>
  <div class="logo-badge" role="img" aria-label="Circular badge with cartoon of Dawson riding his mower"></div>

  <ul class="feature-list">
    <li><svg class="tick" viewBox="0 0 14 14"><circle cx="7" cy="7" r="6" fill="none" stroke="var(--brand-blue)" stroke-width="1.4"/><path d="M4 7.2l2 2 4-4.4" fill="none" stroke="var(--brand-blue)" stroke-width="1.4"/></svg><b>Quality-</b> Working with my Dad,<br>he has 20 years experience</li>
    <li><svg class="tick" viewBox="0 0 14 14"><circle cx="7" cy="7" r="6" fill="none" stroke="var(--brand-blue)" stroke-width="1.4"/><path d="M4 7.2l2 2 4-4.4" fill="none" stroke="var(--brand-blue)" stroke-width="1.4"/></svg><b>Care-</b> I will treat your yard like my own</li>
    <li><svg class="tick" viewBox="0 0 14 14"><circle cx="7" cy="7" r="6" fill="none" stroke="var(--brand-blue)" stroke-width="1.4"/><path d="M4 7.2l2 2 4-4.4" fill="none" stroke="var(--brand-blue)" stroke-width="1.4"/></svg><b>Mower-</b> Half the weight of other mowers<br>&amp; doesn't blow clippings into mulch</li>
  </ul>

  <h2 class="extras-heading">EXTRAS</h2>

  <ul class="extras-list">
    <li><svg class="tick" viewBox="0 0 14 14"><circle cx="7" cy="7" r="6" fill="none" stroke="var(--brand-blue)" stroke-width="1.4"/><path d="M4 7.2l2 2 4-4.4" fill="none" stroke="var(--brand-blue)" stroke-width="1.4"/></svg><b>Bagging-</b> I can bag the clippings</li>
    <li><svg class="tick" viewBox="0 0 14 14"><circle cx="7" cy="7" r="6" fill="none" stroke="var(--brand-blue)" stroke-width="1.4"/><path d="M4 7.2l2 2 4-4.4" fill="none" stroke="var(--brand-blue)" stroke-width="1.4"/></svg><b>Dog poop-</b> I can scoop it for you</li>
    <li><svg class="tick" viewBox="0 0 14 14"><circle cx="7" cy="7" r="6" fill="none" stroke="var(--brand-blue)" stroke-width="1.4"/><path d="M4 7.2l2 2 4-4.4" fill="none" stroke="var(--brand-blue)" stroke-width="1.4"/></svg><b>One time cut-</b> While you are on vacation</li>
  </ul>

  <p class="season-offer">One Free Cut With Commitment<br>To A Full 26 Week Season</p>

  <p class="phone">
    <svg width="28" height="28" viewBox="0 0 28 28"><circle cx="14" cy="14" r="12.5" fill="none" stroke="var(--brand-blue)" stroke-width="2"/><path d="M9.5 7.5c-1.5 1-1.8 2.8-.6 5.2 1.4 2.8 3.6 5 6.4 6.4 2.4 1.2 4.2.9 5.2-.6l-2.6-2.4-1.8 1.1c-1.6-.8-2.9-2.1-3.7-3.7l1.1-1.8z" fill="var(--brand-blue)"/></svg>
    555-271-0936
  </p>

  <div class="stamp-box"></div>
  <div class="address-line" style="top:305px"></div>
  <div class="address-line" style="top:342px"></div>
  <div class="address-line" style="top:380px"></div>
</section>

</body>
</html>
```